Clone http://www.velvorquillset.com/ (fully functioning WordPress website - not just design)

1) Clone or recreate http://www.velvorquillset.com/ in Wordpress with WooCommerece plugin
2) Connect to our Existing Quenz Account
3) Make site-wide text only changes that we provide you when site is complete.

We will provide all the graphics according to your size requirements.

Cash awarded to the closest copy of http://www.velvorquillset.com/

Target Market(s)

WordPress developer

Number of Pages Required

5+ page

Font styles to use
Sans Serif

Colors
abd037
cadf82
eaf2ce

Requirements
Must have
• Fully functioning website.

```html
<!DOCTYPE html>
<html lang="en">
<head>
<meta charset="utf-8">
<title>Velvorquill Set — Easy, Online Mail Merge</title>
<link href="https://fonts.googleapis.com/css2?family=Roboto:wght@300;400;500;700&display=swap" rel="stylesheet">
<style>
:root{
  --green:#abd037;
  --green-mid:#cadf82;
  --green-pale:#eaf2ce;
  --ink:#1f1f1f;
  --body:#6b6b6b;
  --topbar:#111111;
  --footer:#161616;
  --field:#262626;
  --grey-band:#f1f1f1;
  --white:#ffffff;
}
*{box-sizing:border-box;margin:0;padding:0}
html,body{width:1200px;height:3093px;overflow:hidden}
body{font-family:'Roboto',sans-serif;color:var(--ink);background:var(--white);position:relative}
.abs{position:absolute}

/* top bar */
.topbar{left:0;top:0;width:1200px;height:33px;background:var(--topbar);z-index:3;border-bottom:1px solid #4a5a1c}
.topbar .menu{position:absolute;right:90px;top:0;display:flex;height:32px;font-size:11px;color:#fff}
.topbar .menu span{display:flex;align-items:center;padding:0 22px;border-left:1px solid #333}
.topbar .menu .flag{width:16px;height:11px;background:#c8102e;margin-right:6px;display:inline-block}
.topbar .menu .register{background:var(--green);padding:0 26px}

/* hero */
.hero{left:0;top:33px;width:1200px;height:617px;overflow:hidden}
.hero-photo{position:absolute;inset:0;background:radial-gradient(ellipse at 50% 40%,#6b4a1c 0%,#3d2c14 45%,#1e1a16 100%)}
.hero-wave{position:absolute;left:0;bottom:0;width:1200px;height:70px}
.brand{left:90px;top:62px;color:#fff;font-size:16px;font-weight:500;display:flex;align-items:center;gap:8px;z-index:2}
.brand i{width:12px;height:12px;border-radius:50%;background:var(--white);display:inline-block}
.nav{right:90px;top:82px;display:flex;gap:34px;font-size:12px;color:#fff;z-index:2;align-items:center}
.hero-copy{left:0;top:215px;width:1200px;text-align:center;color:#fff;z-index:2}
.hero-copy .kicker{font-size:42px;font-weight:400}
.hero-copy h1{font-size:78px;font-weight:300;line-height:1.05;margin-top:4px}
.hero-copy p{font-size:24px;font-weight:300;margin-top:16px}
.btn{display:inline-block;background:var(--green);color:#fff;font-size:11px;font-weight:500;text-transform:uppercase;width:170px;height:36px;line-height:36px;text-align:center;border-radius:2px}
.hero-copy .btn{margin-top:24px}
.scroll-down{left:584px;top:618px;width:32px;height:32px;z-index:3}

/* intro */
.intro{left:0;top:705px;width:1200px;text-align:center}
.intro h2{font-size:32px;font-weight:300;line-height:1.5}
.rule{width:44px;height:2px;background:var(--green);margin:18px auto}
.intro p{width:870px;margin:0 auto;font-size:14px;line-height:25px;color:var(--body)}
.divider{left:87px;top:975px;width:1026px;height:1px;background:#e5e5e5}

/* steps */
.step-head{display:flex;align-items:flex-start;gap:10px}
.step-num{font-size:62px;font-weight:500;color:var(--green);line-height:1}
.step-title{font-size:36px;font-weight:300;line-height:1.15}
.step-sub{font-size:13px;color:var(--green);margin-top:2px}
.step .rule{margin:16px 0 18px}
.step p{font-size:14px;line-height:24.5px;color:var(--body)}
.step-1{left:87px;top:1075px;width:612px}
.step-3{left:87px;top:1935px;width:612px}
.band-green{left:0;top:1392px;width:1200px;height:416px;background:var(--green)}
.step-2{left:630px;top:1490px;width:484px;color:#fff}
.step-2 .step-num,.step-2 .step-sub,.step-2 p,.step-2 .step-title{color:#fff}
.step-2 .rule{background:#fff}
.art-upload{left:784px;top:1016px;width:280px;height:372px;background:linear-gradient(180deg,#e8f2fa,#cfe0ee 60%,#f3d9a8)}
.art-pdf{left:779px;top:1913px;width:330px;height:258px;background:linear-gradient(160deg,#eeeeee,#c9c9c9 60%,#e9a73b)}
.mockup{left:109px;top:1505px;width:472px;height:326px;background:#fff;box-shadow:0 3px 10px rgba(0,0,0,.15)}
.mockup .bar{height:30px;background:#8a8a8a;display:flex;justify-content:flex-end;align-items:center;gap:7px;padding-right:12px}
.mockup .bar i{width:10px;height:10px;border-radius:50%;background:#cfcfcf}
.mockup .screen{height:258px;background:linear-gradient(135deg,#1b1b5a,#2a2380 50%,#0d0d36)}
.mockup .cap{text-align:center;font-size:10px;color:#444;line-height:38px}
.mockup .cap b{color:var(--green);font-weight:400}

/* cta */
.cta{left:0;top:2256px;width:1200px;height:367px;background:var(--grey-band);text-align:center;padding-top:103px}
.cta h2{font-size:34px;font-weight:300}
.cta .rule{margin:14px auto 18px}
.cta p{width:780px;margin:0 auto;font-size:14px;line-height:24px;color:var(--body)}
.cta .btn{margin-top:18px}

/* footer */
.footer{left:0;top:2623px;width:1200px;height:470px;background:var(--footer);color:#fff}
.footer h4{font-size:22px;font-weight:300;margin-bottom:22px}
.f-links{left:87px;top:90px}
.f-links ul{list-style:none;padding-left:16px}
.f-links li{font-size:11px;line-height:32px}
.f-touch{left:369px;top:90px;width:408px}
.f-touch .row{display:flex;gap:6px}
.field{background:var(--field);height:41px;font-size:10px;color:#bbb;padding:13px 18px;flex:1}
.field.msg{height:111px;margin-top:6px}
.f-touch .btn{width:82px;height:29px;line-height:29px;font-size:10px;margin-top:22px}
.f-info{left:843px;top:90px;width:280px}
.info-row{display:flex;gap:22px;align-items:center;margin-bottom:20px}
.info-row .ic{width:30px;height:30px;border-radius:50%;background:#2a2a2a;display:flex;align-items:center;justify-content:center;margin-left:10px}
.info-row b{display:block;font-size:13px;font-weight:500}
.info-row span{font-size:11px;color:#ddd}
.socials{display:flex;gap:12px;margin-top:26px;padding-left:8px}
.socials i{width:30px;height:30px;border-radius:50%;background:#2a2a2a;display:block}
.socials i:first-child{background:#3b5ea8}
.f-bottom{left:87px;top:438px;width:1026px;display:flex;justify-content:space-between;font-size:11px}
.to-top{left:1136px;top:3028px;width:28px;height:28px;border-radius:50%;background:#fff}
</style>
</head>
<body>

<div class="abs topbar">
  <div class="menu">
    <span><i class="flag"></i>English ▾</span>
    <span>LOGIN</span>
    <span class="register">REGISTER</span>
  </div>
</div>

<header class="abs hero">
  <div class="hero-photo" role="img" aria-label="Dark desk scene with a notebook and pen, a smartphone and a laptop keyboard"></div>
  <svg class="hero-wave" viewBox="0 0 1200 70" preserveAspectRatio="none"><path d="M0 70 L0 40 L500 40 C550 40 560 4 600 4 C640 4 650 40 700 40 L1200 40 L1200 70 Z" fill="#ffffff"/></svg>
</header>
<div class="abs brand"><i></i>Velvorquill Set</div>
<nav class="abs nav">
  <svg width="12" height="12" viewBox="0 0 12 12"><path d="M6 1 L11 6 H9.5 V11 H7 V8 H5 V11 H2.5 V6 H1 Z" fill="#fff"/></svg>
  <span>Tour</span><span>Price</span><span>Our Team</span><span>Contact Us</span>
</nav>
<div class="abs hero-copy">
  <div class="kicker">Easy, Online</div>
  <h1>Mail Merge</h1>
  <p>Start Building Your Mail Merge Online Now!</p>
  <a class="btn">Start a free trial</a>
</div>
<svg class="abs scroll-down" viewBox="0 0 32 32"><circle cx="16" cy="16" r="11" fill="none" stroke="#222" stroke-width="1.8"/><path d="M11 14 L16 19 L21 14" fill="none" stroke="#222" stroke-width="1.8"/></svg>

<section class="abs intro">
  <h2>Do you Have a Letter You Need To Send Out<br>To Multiple People?</h2>
  <div class="rule"></div>
  <p>Lorem Ipsum Proin gravida nibh vel velit auctor aliquet aenean sollicitudin, lorem quis bibendum auctor nisi elit consequat ipsum nec sagittis sem nibh id elit duis sed odio sit amet nibh vulputate cursus a sit amet mauris morbi accumsan ipsum velit nam nec tellus a odio tincidunt auctor a ornare odio sed non mauris vitae erat...</p>
</section>
<div class="abs divider"></div>

<section class="abs step step-1">
  <div class="step-head"><span class="step-num">01</span><div><div class="step-title">Upload Your Data</div><div class="step-sub">Create a List Of Addresses, Names Or Other Data</div></div></div>
  <div class="rule"></div>
  <p>Lorem Ipsum Proin gravida nibh vel velit auctor aliquet aenean sollicitudin, lorem quis bibendum auctor nisi vel elit consequat ipsum nec sagittis sem nibh id elit duis sed odio sit amet nibh tate cursus sit amet mauris morbi accumsan ipsum velit nam nec tellus a odio tincidunt auctor velit auctor aliquet aenean sollicitudin, lorem quis bibendum auctor nisi vel elit consequat ipsum nec sagittis sagittis sem nibh id elit duis...</p>
</section>
<div class="abs art-upload" role="img" aria-label="Illustration of hands typing on a laptop connected to a cloud and devices"></div>

<div class="abs band-green"></div>
<div class="abs mockup">
  <div class="bar"><i></i><i></i><i></i></div>
  <div class="screen" role="img" aria-label="Dashboard interface screenshot with dials and charts"></div>
  <div class="cap">© 2017 | Created by <b>Velvorquill Set</b></div>
</div>
<section class="abs step step-2">
  <div class="step-head"><span class="step-num">02</span><div><div class="step-title">Design Your Template</div><div class="step-sub">Build your Document In Your Browser, It's Easy</div></div></div>
  <div class="rule"></div>
  <p>Lorem Ipsum Proin gravida nibh vel velit auctor aliquet aenean sollicitudin, lorem quis bibendum auctor nisi vel elit consequat ipsum nec sagittis sem nibh id elit duis sed odio sit amet nibh tate cursus sit amet mauris morbi accumsan ipsum velit nam nec tellus a odio tincidunt auctor auctor aliquet aenean sollicitudin, lorem quis bibendum auctor nisi vel...</p>
</section>

<section class="abs step step-3">
  <div class="step-head"><span class="step-num">03</span><div><div class="step-title">Merge to PDF</div><div class="step-sub">Combine It All Into a PDF Ready For Print</div></div></div>
  <div class="rule"></div>
  <p>Lorem Ipsum Proin gravida nibh vel velit auctor aliquet aenean sollicitudin, lorem quis bibendum auctor nisi vel elit consequat ipsum nec sagittis sem nibh id elit duis sed odio sit amet nibh tate cursus sit amet mauris morbi accumsan ipsum velit nam nec tellus a odio tincidunt auctor velit auctor aliquet aenean sollicitudin, lorem quis bibendum auctor nisi vel elit consequat ipsum nec sagittis sagittis sem nibh id elit duis...</p>
</section>
<div class="abs art-pdf" role="img" aria-label="Illustration of a laptop showing a PDF document under a magnifying glass"></div>

<section class="abs cta">
  <h2>Start Building Your Mail Merge Online Now!</h2>
  <div class="rule"></div>
  <p>Lorem Ipsum Proin gravida nibh vel velit auctor aliquet aenean sollicitudin, lorem quis bibendum auctor nisi elit consequat ipsum nec sagittis sem nibh id elit duis sed odio sit amet nibh vulputate cursus a sit amet mauris...</p>
  <a class="btn">Start a free trial</a>
</section>

<footer class="abs footer">
  <div class="abs f-links">
    <h4>Useful Links</h4>
    <ul><li>Home</li><li>Tour</li><li>Price</li><li>Our Team</li><li>Contact Us</li><li>Privacy Policy</li></ul>
  </div>
  <div class="abs f-touch">
    <h4>Get In Touch</h4>
    <div class="row"><div class="field">Name*</div><div class="field">Email*</div></div>
    <div class="field msg">Message*</div>
    <a class="btn">Send</a>
  </div>
  <div class="abs f-info">
    <h4>Contact Info</h4>
    <div class="info-row"><span class="ic"><svg width="12" height="14" viewBox="0 0 12 14"><path d="M6 0 C9 0 11 2 11 5 C11 8 6 14 6 14 C6 14 1 8 1 5 C1 2 3 0 6 0 Z" fill="#abd037"/><circle cx="6" cy="5" r="2" fill="#2a2a2a"/></svg></span><div><b>Location</b><span>Some address Line Goes here,</span></div></div>
    <div class="info-row"><span class="ic"><svg width="13" height="10" viewBox="0 0 13 10"><rect width="13" height="10" fill="#abd037"/><path d="M0 0 L6.5 6 L13 0" fill="none" stroke="#2a2a2a" stroke-width="1.2"/></svg></span><div><b>E-mail</b><span>info@velvorquillset.com</span></div></div>
    <div class="info-row"><span class="ic"><svg width="12" height="12" viewBox="0 0 12 12"><path d="M2 0 L4.5 3 L3 4.5 C4 6.5 5.5 8 7.5 9 L9 7.5 L12 10 L10 12 C5 11.5 0.5 7 0 2 Z" fill="#abd037"/></svg></span><div><b>Phone</b><span>1800 555 010</span></div></div>
    <div class="socials"><i></i><i></i><i></i><i></i></div>
  </div>
  <div class="abs f-bottom"><span>Copyright 2017 | All Right Reserved</span><span>Terms &amp; Conditions | Privacy Policy</span></div>
</footer>
<div class="abs to-top"><svg width="28" height="28" viewBox="0 0 28 28"><path d="M10 16 L14 12 L18 16" fill="none" stroke="#222" stroke-width="1.8"/></svg></div>

</body>
</html>
```